Austrian finance und insurance broker needs business card design

We Need a serious looking Design for Business Card. we consult private and corporates customers in finance and insurance questions. the final design should express security and experience. We consult customers in questions of loans, Investments and insurance and have a wide range of Banks to offer. We compare several offers and select the best for our customers.

Target Market(s)

private and coporate customers with efforts in Money and insurance

Industry/Entity Type

Insurance Broker

Contact Information for Business Card

Bernhard Aigner
Geschäftsführer
staatl. geprüfter Vermögensberater und Versicherungsmakler
Tel: 0664 521 8409
office@der-brandl.at
www.der-brandl.at
Leopold Hainz Gasse 14
2183 Melkstetten
GISA Nr. 48270315 u. 51736048 (backside)

Font styles to use
Serif
Sans Serif

Requirements
Must have
• logo (designcrowd zip) and all Details
Nice to have
• makler logo design, maybe a 2 coloured Version is possible

```html
<!DOCTYPE html>
<html lang="de">
<head>
<meta charset="utf-8">
<title>BA Vermögensberatung GmbH – Visitenkarte</title>
<link rel="stylesheet" href="https://fonts.googleapis.com/css2?family=Montserrat:wght@600;700&family=Roboto:wght@400;500;700&display=swap">
<style>
  :root {
    --bg: #1b1b1b;
    --brand-blue: #2f5fb3;
    --brand-blue-light: #3d6cc0;
    --ink-grey: #5a5a5a;
    --rule-grey: #6b6b6b;
    --card-white: #f6f6f6;
    --seal-red: #a51f22;
    --faint-ring: #e6e7f4;
  }
  * { box-sizing: border-box; margin: 0; padding: 0; }
  html, body { width: 1200px; height: 1200px; overflow: hidden; background: var(--bg); }
  .stage { position: relative; width: 1200px; height: 1200px; }

  .card {
    position: absolute; left: 150px; width: 900px; height: 515px;
    border-radius: 22px; overflow: hidden;
  }

  /* back side */
  .card--back {
    top: 60px;
    background: linear-gradient(135deg, var(--brand-blue) 0%, var(--brand-blue-light) 100%);
    color: #fff;
  }
  .card--back .deco-ring {
    position: absolute; right: -70px; top: 60px; width: 380px; height: 380px;
    border-radius: 50%; border: 14px solid rgba(255,255,255,0.1);
  }
  .lockup { position: absolute; display: flex; align-items: center; white-space: nowrap; }
  .card--back .lockup { left: 220px; top: 170px; }
  .lockup__mark { width: 110px; height: 110px; border-radius: 50%; border: 7px solid currentColor; flex: none; }
  .lockup__divider { width: 4px; height: 116px; margin: 0 22px; background: currentColor; flex: none; }
  .lockup__name {
    font-family: "Montserrat", sans-serif; font-weight: 700; font-size: 28px; letter-spacing: 0.3px;
  }
  .lockup__name small { font-size: 20px; }
  .lockup__tagline {
    font-family: "Montserrat", sans-serif; font-weight: 600; font-size: 18px; margin-top: 6px;
  }
  .card--back .address {
    position: absolute; left: 0; right: 0; bottom: 40px; text-align: center;
    font-family: "Roboto", sans-serif; font-weight: 500; font-size: 20px;
  }

  /* front side */
  .card--front { top: 625px; background: var(--card-white); color: var(--ink-grey); }
  .card--front .deco-ring {
    position: absolute; right: -30px; top: 60px; width: 300px; height: 300px;
    border-radius: 50%; border: 12px solid var(--faint-ring);
  }
  .card--front .lockup { left: 60px; top: 45px; color: var(--rule-grey); }
  .card--front .lockup__mark { border-color: var(--brand-blue); }
  .card--front .lockup__name { color: var(--brand-blue); }
  .card--front .lockup__tagline { color: var(--ink-grey); }

  .person { position: absolute; left: 60px; top: 212px; font-family: "Roboto", sans-serif; }
  .person__name { font-weight: 700; font-size: 34px; color: var(--ink-grey); }
  .person__name .surname { color: var(--brand-blue); }
  .person__role { font-size: 21px; margin-top: 6px; }
  .person__qual { font-size: 21px; margin-top: 2px; }

  .rule { position: absolute; height: 2px; }
  .rule--grey { left: 60px; top: 340px; width: 430px; background: var(--rule-grey); }
  .rule--blue { left: 490px; top: 340px; width: 360px; background: var(--brand-blue); }

  .contact { position: absolute; left: 60px; top: 358px; list-style: none; font-family: "Roboto", sans-serif; font-size: 22px; }
  .contact li { display: flex; align-items: center; gap: 12px; height: 34px; }
  .contact svg { width: 20px; height: 20px; fill: none; stroke: var(--brand-blue); stroke-width: 2; }
  .contact .icon-phone { fill: var(--brand-blue); stroke: none; }

  .partner { position: absolute; right: 60px; top: 385px; display: flex; align-items: center; gap: 18px; }
  .partner__name { font-family: "Roboto", sans-serif; font-weight: 700; font-size: 20px; letter-spacing: 1.5px; color: var(--seal-red); }
  .partner__badge { width: 62px; height: 62px; border-radius: 50%; background: var(--seal-red); }

  .band { position: absolute; bottom: 0; height: 16px; }
  .band--blue { left: 0; width: 50%; background: var(--brand-blue); }
  .band--grey { right: 0; width: 50%; background: var(--rule-grey); }
</style>
</head>
<body>
<main class="stage">

  <section class="card card--back" aria-label="Rückseite">
    <div class="deco-ring"></div>
    <div class="lockup">
      <div class="lockup__mark"></div>
      <div class="lockup__divider"></div>
      <div>
        <div class="lockup__name">BA Vermögensberatung <small>GmbH</small></div>
        <div class="lockup__tagline">Finanzieren, Versichern, Vorsorgen</div>
      </div>
    </div>
    <p class="address">Leopold Hainz Gasse 14, 2183 Melkstetten, GISA Nr. 48270315 u. 51736048 (backside)</p>
  </section>

  <section class="card card--front" aria-label="Vorderseite">
    <div class="deco-ring"></div>
    <div class="lockup">
      <div class="lockup__mark"></div>
      <div class="lockup__divider"></div>
      <div>
        <div class="lockup__name">BA Vermögensberatung <small>GmbH</small></div>
        <div class="lockup__tagline">Finanzieren, Versichern, Vorsorgen</div>
      </div>
    </div>

    <div class="person">
      <div class="person__name">Bernhard <span class="surname">Aigner</span></div>
      <div class="person__role">Geschäftsführer</div>
      <div class="person__qual">staatl. geprüfter Vermögensberater und Versicherungsmakler</div>
    </div>

    <div class="rule rule--grey"></div>
    <div class="rule rule--blue"></div>

    <ul class="contact">
      <li>
        <svg class="icon-phone" viewBox="0 0 24 24"><path d="M6.6 10.8a15.1 15.1 0 0 0 6.6 6.6l2.2-2.2a1 1 0 0 1 1-.25 11.4 11.4 0 0 0 3.6.57 1 1 0 0 1 1 1V20a1 1 0 0 1-1 1A17 17 0 0 1 3 4a1 1 0 0 1 1-1h3.5a1 1 0 0 1 1 1c0 1.25.2 2.45.57 3.57a1 1 0 0 1-.25 1z"/></svg>
        0664 521 8409
      </li>
      <li>
        <svg viewBox="0 0 24 24"><rect x="3" y="5" width="18" height="14"/><path d="M3 5l9 8 9-8"/></svg>
        office@der-brandl.at
      </li>
      <li>
        <svg viewBox="0 0 24 24"><circle cx="12" cy="12" r="9"/><path d="M3 12h18M12 3c3 3 3 15 0 18M12 3c-3 3-3 15 0 18"/></svg>
        www.der-brandl.at
      </li>
    </ul>

    <div class="partner">
      <span class="partner__name">VERSIRO MAKLERPARTNER</span>
      <div class="partner__badge"></div>
    </div>

    <div class="band band--blue"></div>
    <div class="band band--grey"></div>
  </section>

</main>
</body>
</html>
```